KTM Inquiry Partners PLLC
Law Firm Conducting Investigations
KTM Inquiry Partners PLLC -
Creative Brief
Professional
Dale Morrow
Attorney
21430 SW 3rd Ave, Suite C2-418 Bellevue, WA 98006
dale@ktminquiry-example.com
www.ktminquiry-example.com
I would like the card to be simple, clean and professional. Please use color schemes that match the logo, but don't use too much gold.
The back of the card should be blank.

```html
<!DOCTYPE html>
<html lang="en">
<head>
<meta charset="utf-8">
<title>Dale Morrow – Business Card</title>
<link rel="stylesheet" href="https://fonts.googleapis.com/css2?family=Tinos:wght@400;700&display=swap">
<style>
  :root {
    --backdrop: #ece9e3;
    --card: #ffffff;
    --ink: #1f1f1f;
    --name: #4a3c22;
    --title: #8a8a8a;
    --gold: #b8934a;
    --gold-soft: #d9c08a;
    --rule: #6b6b6b;
  }
  * { margin: 0; padding: 0; box-sizing: border-box; }
  html, body {
    width: 1200px;
    height: 797px;
    overflow: hidden;
    background: var(--backdrop);
    font-family: "Tinos", "Times New Roman", serif;
  }
  .card {
    position: absolute;
    left: 50px;
    top: 92px;
    width: 1100px;
    height: 612px;
    background: var(--card);
    border-radius: 48px;
    box-shadow: 0 6px 24px rgba(0,0,0,0.12);
    overflow: hidden;
  }
  .card-tab {
    position: absolute;
    left: 0;
    top: 330px;
    width: 16px;
    height: 120px;
    background: linear-gradient(90deg, var(--gold), var(--gold-soft));
    border-radius: 0 10px 10px 0;
  }
  .identity {
    position: absolute;
    left: 125px;
    top: 55px;
    width: 360px;
    text-align: center;
  }
  .identity-name {
    font-weight: 700;
    font-size: 66px;
    line-height: 1;
    color: var(--name);
    letter-spacing: 1px;
    white-space: nowrap;
  }
  .identity-rule {
    height: 3px;
    margin: 6px 0 4px;
    background: linear-gradient(90deg, transparent, var(--rule) 15%, var(--rule) 85%, transparent);
  }
  .identity-title {
    font-size: 50px;
    line-height: 1.05;
    color: var(--title);
  }
  .contact {
    position: absolute;
    left: 125px;
    top: 322px;
    font-size: 30px;
    line-height: 42px;
    color: var(--ink);
    list-style: none;
  }
  .divider {
    position: absolute;
    left: 580px;
    top: 80px;
    width: 3px;
    height: 500px;
    background: linear-gradient(180deg, transparent, var(--rule) 30%, var(--rule) 70%, transparent);
  }
  .firm {
    position: absolute;
    left: 640px;
    top: 282px;
    display: flex;
    align-items: center;
    gap: 18px;
  }
  .firm-mark {
    width: 46px;
    height: 46px;
    background: var(--gold);
  }
  .firm-name {
    font-size: 38px;
    color: var(--gold);
    white-space: nowrap;
  }
</style>
</head>
<body>
  <main class="card">
    <div class="card-tab"></div>

    <header class="identity">
      <h1 class="identity-name">Dale Morrow</h1>
      <div class="identity-rule"></div>
      <p class="identity-title">Attorney</p>
    </header>

    <ul class="contact">
      <li>21430 SW 3rd Ave, Suite C2-418</li>
      <li>Bellevue, WA 98006</li>
      <li>Phone: 425-555-0143</li>
      <li>dale@ktminquiry-example.com</li>
      <li>www.ktminquiry-example.com</li>
    </ul>

    <div class="divider"></div>

    <div class="firm">
      <span class="firm-mark"></span>
      <span class="firm-name">KTM Inquiry Partners</span>
    </div>
  </main>
</body>
</html>
```